Quarvex Power Point Template - Institutional Presentation

Develop a comprehensive template for a corporate presentation power point.

The presentation will be aimed to institutional investors.

Style to be modern and contemporary. Use of icons and images welcome but not to much.

It would be great if you could develop the layout/style for the content in the following slides:

- Cover
- Section title
- Slide with title and bullet points on one side and two text boxes on the other side
- Slide with line chart and pie chart
- Slide with table

Should we like the slides above we will then develop the rest of the template.

We may then need to have a dark-background version - but this will be invoiced separately.

Target Market(s)

Corporate institutional investors

Industry/Entity Type

Finance

Font styles to use
Serif
Sans Serif

Colors
3176b5
0255a3
cee9f5
86cae7
33a6d7
0792cd
33b8a4
00a990
86cfc6

Requirements
Must have
• Mostly white background with minimal objects
Nice to have
• Use of photos, but not to much.

```html
<!DOCTYPE html>
<html lang="en">
<head>
<meta charset="utf-8">
<title>Quarvex – Finance Presentation Template</title>
<link href="https://fonts.googleapis.com/css2?family=Bebas+Neue&family=Open+Sans:wght@400;600;700&display=swap" rel="stylesheet">
<style>
:root{
  --navy:#1d2a4a;
  --ink:#2b3550;
  --blue:#0792cd;
  --blue-deep:#0255a3;
  --sky:#33a6d7;
  --ice:#cee9f5;
  --teal:#33b8a4;
  --aqua:#4cc3cc;
  --aqua-soft:#86cfc6;
  --paper:#ffffff;
  --panel:#f6fafc;
  --muted:#8a93a3;
  --line:#dfe7ee;
}
*{box-sizing:border-box;margin:0;padding:0}
html,body{width:1200px;height:1000px;overflow:hidden}
body{font-family:"Open Sans",Arial,sans-serif;color:var(--ink);
  background:radial-gradient(ellipse at 72% 42%,#2f8ea6 0%,#0f4e66 30%,#06202d 62%,#041722 100%);position:relative}
.floor{position:absolute;left:0;top:940px;width:1200px;height:60px;background:linear-gradient(#2aa7c4,#7fd3e6)}
.slide{position:absolute;width:418px;height:234px;background:var(--paper);overflow:hidden}
.slide .stage{position:absolute;left:105px;top:0;right:0;bottom:0;background:var(--panel)}
.slide .topline{position:absolute;left:105px;right:0;top:4px;height:2px;background:var(--aqua)}
.badge{position:absolute;background:var(--navy);color:#fff;font-weight:700;letter-spacing:1.5px;font-size:6px;padding:3px 7px}
.slide .badge.corner{right:6px;top:4px}
.pageno{position:absolute;right:16px;bottom:6px;font-size:5px;color:var(--muted)}
.pageno::before{content:"";position:absolute;right:0;top:-6px;width:14px;height:1.5px;background:var(--aqua)}
.display{font-family:"Bebas Neue",Impact,sans-serif;line-height:.92;color:var(--ink)}
.side-title{position:absolute;left:22px;font-size:18px}
.small{font-size:4.6px;line-height:1.45;color:#555}
.photo{position:absolute}
.s1{left:16px;top:16px}.s2{left:16px;top:256px}.s3{left:16px;top:499px}.s4{left:16px;top:743px}
.s5{left:452px;top:16px}.s6{left:452px;top:256px}.s7{left:452px;top:502px}.s8{left:452px;top:746px}
.cover-title{position:absolute;left:120px;top:98px;font-size:27px}
.cover-title .accent{color:var(--aqua)}
.cover-sub{position:absolute;left:120px;top:160px;font-size:5px;color:#666}
.dark-title{position:absolute;left:52px;top:90px;font-size:27px;color:#fff}
.dark-title .accent{color:var(--aqua)}
.quote-mark{position:absolute;left:222px;top:34px;font-family:"Bebas Neue",sans-serif;font-size:46px;color:var(--teal);line-height:1}
.quote{position:absolute;left:236px;top:66px;width:170px;font-size:12.5px;line-height:1.55;color:#9aa2ae}
.coverage{position:absolute;top:133px;width:78px}
.coverage h4{font-family:"Bebas Neue",sans-serif;font-weight:400;font-size:10px;color:var(--ink);margin-bottom:6px}
.bullets{position:absolute;left:120px;top:30px;width:95px}
.bullets h4{font-family:"Bebas Neue",sans-serif;font-weight:400;font-size:11px;margin-bottom:4px}
.bullets li{list-style:none;position:relative;padding-left:6px;margin-bottom:4px}
.bullets li::before{content:"";position:absolute;left:0;top:2px;width:2px;height:2px;background:var(--blue-deep);border-radius:50%}
.feature{position:absolute;top:28px;width:86px;height:190px;border:1px solid var(--aqua-soft);padding:8px}
.feature h4{font-family:"Bebas Neue",sans-serif;font-weight:400;font-size:9px;line-height:1;margin-bottom:6px}
.chart-title{position:absolute;left:22px;top:118px;font-size:17px}
.donut-label{position:absolute;font-size:4.5px;color:#555;text-align:center}
.donut-label b{display:block;font-family:"Bebas Neue",sans-serif;font-weight:400;font-size:10px;color:var(--ink)}
.table-title{position:absolute;left:22px;top:20px;font-size:17px}
.table-title::after{content:"";display:block;width:14px;height:1.5px;background:var(--aqua);margin-top:5px}
.smart-table{position:absolute;left:28px;top:62px;border-collapse:collapse;font-size:6px}
.smart-table th{color:#fff;font-weight:600;width:50px;height:18px;font-size:5.5px}
.smart-table td{height:21px;text-align:center;border:1px solid var(--line);color:#333}
.smart-table td.rowhead{width:57px;text-align:left;padding-left:4px;font-size:5px;color:#555;background:#f3f6f8}
.smart-table th.blank{background:transparent;width:57px}
.zoom{position:absolute;border-radius:50%;border:6px solid #e9f5fa;overflow:hidden;box-shadow:0 0 0 2px rgba(0,0,0,.15)}
.zoom-stat{left:860px;top:38px;width:316px;height:316px;background:#f4f9fc}
.zoom-photo{left:858px;top:456px;width:320px;height:320px}
.zoom-value{position:absolute;left:50%;top:57%;transform:translateX(-50%);font-family:"Bebas Neue",sans-serif;font-size:50px;color:#fff}
.overlay{position:absolute;left:0;top:0;pointer-events:none}
</style>
</head>
<body>
<div class="floor"></div>

<!-- Cover, light -->
<section class="slide s1">
  <div class="photo" role="img" aria-label="Photo of two business people reviewing a tablet" style="left:0;top:0;width:105px;height:234px;background:linear-gradient(135deg,#c9b7a8,#6d6a70 55%,#2f3440)"></div>
  <span class="badge" style="left:122px;top:78px;font-size:7px">QUARVEX</span>
  <h1 class="display cover-title">Finance<br><span class="accent">Presentation</span> Template</h1>
  <p class="cover-sub">Lorem ipsum dolor sit amet</p>
  <span class="pageno">SLIDE / 1</span>
</section>

<!-- Cover, dark -->
<section class="slide s2" style="background:#2a2b2f">
  <div class="photo" role="img" aria-label="Dimmed photo of business people meeting at a laptop" style="inset:0;background:linear-gradient(120deg,#3c3c40,#55514f 45%,#2a2a2d)"></div>
  <span class="badge" style="left:52px;top:70px;font-size:7px">QUARVEX</span>
  <h1 class="display dark-title"><span class="accent">Finance</span><br>Presentation Template</h1>
  <p class="cover-sub" style="left:52px;top:152px;color:#ddd">Lorem ipsum dolor sit amet</p>
  <span style="position:absolute;left:52px;top:194px;width:18px;height:1.5px;background:var(--aqua)"></span>
</section>

<!-- Section title -->
<section class="slide s3">
  <div class="topline" style="left:210px"></div>
  <span class="badge corner">QUARVEX</span>
  <h2 class="display side-title" style="top:122px">Our<br>Section<br>Title</h2>
  <div class="photo" role="img" aria-label="Photo of a businessman facing a city skyline under a world map sky" style="left:105px;top:0;width:105px;height:234px;background:linear-gradient(#bcd9ec,#e3eef6 40%,#f3d9cf 75%,#e9b8a4)"></div>
  <span class="quote-mark">“</span>
  <p class="display quote">Lorem ipsum dolor sit amet, consectetur adipiscing elit. Quisque eleifend sapien mauris. Aenean nec bibendum justo. Vivamus malesuada ac diam ut malesuada.</p>
  <span class="pageno">SLIDE / 3</span>
</section>

<!-- Bullets and text boxes -->
<section class="slide s4">
  <div class="stage" style="background:#fff"></div>
  <div class="topline"></div>
  <span class="badge corner">QUARVEX</span>
  <h2 class="display side-title" style="top:122px">Another<br>Cool Title<br>For This<br>Section</h2>
  <div class="bullets small">
    <h4>Subtitle</h4>
    <ul>
      <li>Lorem ipsum dolor sit amet, consectetur adipiscing elit.</li>
      <li>Morbi a commodo ipsum. Vestibulum rutrum tincidunt scelerisque. Donec eu ex justo.</li>
      <li>Duis rutrum porttitor risus. Morbi a turpis viverra congue erat in gravida.</li>
      <li>Praesent ut sagittis metus. Curabitur ligula neque, tristique et mollis.</li>
      <li>Pellentesque aliquam viverra condimentum.</li>
    </ul>
  </div>
  <div class="feature small" style="left:216px">
    <h4>Features<br>Sample text here</h4>
    <p>Lorem ipsum dolor sit amet, consectetur adipiscing elit. Morbi a commodo ipsum. Vestibulum rutrum tincidunt scelerisque. Donec eu ex justo. Duis rutrum porttitor risus, morbi a turpis viverra congue erat in gravida ipsum.</p>
    <p style="margin-top:6px">Praesent ut sagittis metus. Curabitur ligula neque, tristique et mollis at, rutrum non nunc.</p>
  </div>
  <div class="feature small" style="left:316px">
    <h4>Features<br>Sample text here</h4>
    <p>Lorem ipsum dolor sit amet, consectetur adipiscing elit. Morbi a commodo ipsum. Vestibulum rutrum tincidunt scelerisque. Donec eu ex justo. Duis rutrum porttitor risus, morbi a turpis viverra congue erat in gravida ipsum.</p>
    <p style="margin-top:6px">Praesent ut sagittis metus. Curabitur ligula neque, tristique et mollis at, rutrum non nunc.</p>
  </div>
  <span class="pageno">SLIDE / 4</span>
</section>

<!-- National coverage -->
<section class="slide s5">
  <div class="stage"></div><div class="topline"></div>
  <span class="badge corner">QUARVEX</span>
  <h2 class="display side-title" style="top:126px;font-size:16px">Our<br>National<br>Coverage</h2>
  <svg width="418" height="234" style="position:absolute;left:0;top:0">
    <g fill="none" stroke="var(--ice)" stroke-width="5">
      <circle cx="162" cy="84" r="37" stroke-dasharray="116 233" transform="rotate(-90 162 84)"/>
      <circle cx="258" cy="84" r="37" stroke-dasharray="81 233" transform="rotate(-90 258 84)"/>
      <circle cx="353" cy="84" r="37" stroke-dasharray="209 233" transform="rotate(-90 353 84)"/>
    </g>
    <g fill="var(--blue)"><circle cx="162" cy="84" r="33"/><circle cx="258" cy="84" r="33"/><circle cx="353" cy="84" r="33"/></g>
    <g fill="none" stroke="#fff" stroke-width="1.2">
      <path d="M162 83c-4-5-6-8-6-11a6 6 0 0 1 12 0c0 3-2 6-6 11z"/><circle cx="162" cy="72" r="2"/>
      <rect x="250" y="67" width="16" height="10" rx="1"/><path d="M247 80h22"/>
      <rect x="345" y="67" width="16" height="11" rx="1"/><path d="M353 70v6m-3-3l3 3 3-3"/>
    </g>
    <g font-family="Bebas Neue, sans-serif" font-size="14" fill="#fff" text-anchor="middle">
      <text x="162" y="110">50%</text><text x="258" y="110">35%</text><text x="353" y="110">90%</text>
    </g>
  </svg>
  <div class="coverage small" style="left:131px"><h4>Where to find us</h4>Lorem ipsum is simply dummy text of the printing and typesetting industry.</div>
  <div class="coverage small" style="left:223px"><h4>Support time</h4>Lorem ipsum is simply dummy text of the printing and typesetting industry.</div>
  <div class="coverage small" style="left:314px"><h4>Downloads</h4>Lorem ipsum is simply dummy text of the printing and typesetting industry.</div>
  <span class="pageno">SLIDE / 5</span>
</section>

<!-- Bar chart -->
<section class="slide s6">
  <div class="stage"></div><div class="topline"></div>
  <span class="badge corner">QUARVEX</span>
  <h2 class="display chart-title">Chart<br>Smart<br>Art</h2>
  <svg width="418" height="234" style="position:absolute;left:0;top:0" font-family="Open Sans, sans-serif">
    <g stroke="#e3e9ee" stroke-width="0.6">
      <path d="M156 48v124M202 48v124M248 48v124M294 48v124M340 48v124M386 48v124"/>
    </g>
    <g font-size="5" fill="#777">
      <text x="130" y="80">Series One</text><text x="130" y="144">Series Two</text>
      <g text-anchor="middle"><text x="156" y="182">0</text><text x="202" y="182">50</text><text x="248" y="182">100</text><text x="294" y="182">150</text><text x="340" y="182">200</text><text x="386" y="182">250</text></g>
    </g>
    <g font-size="5" fill="#fff" text-anchor="end">
      <rect x="156" y="56" width="37" height="10" fill="var(--aqua)"/><text x="191" y="63">40</text>
      <rect x="156" y="67" width="46" height="10" fill="#33a6b8"/><text x="200" y="74">50</text>
      <rect x="156" y="78" width="133" height="10" fill="var(--blue)"/><text x="287" y="85">145</text>
      <rect x="156" y="89" width="55" height="10" fill="#1a8aa8"/><text x="209" y="96">60</text>
      <rect x="156" y="120" width="74" height="10" fill="var(--aqua)"/><text x="228" y="127">80</text>
      <rect x="156" y="131" width="37" height="10" fill="#33a6b8"/><text x="191" y="138">40</text>
      <rect x="156" y="142" width="179" height="10" fill="var(--blue)"/><text x="333" y="149">195</text>
      <rect x="156" y="153" width="55" height="10" fill="#1a8aa8"/><text x="209" y="160">60</text>
    </g>
    <g font-size="4.5" fill="#777">
      <rect x="194" y="199" width="3" height="3" fill="var(--aqua)"/><text x="199" y="202">Column 1</text>
      <rect x="226" y="199" width="3" height="3" fill="#33a6b8"/><text x="231" y="202">Column 2</text>
      <rect x="258" y="199" width="3" height="3" fill="var(--blue)"/><text x="263" y="202">Column 3</text>
      <rect x="290" y="199" width="3" height="3" fill="#1a8aa8"/><text x="295" y="202">Column 4</text>
    </g>
  </svg>
  <span class="pageno">SLIDE / 6</span>
</section>

<!-- Donut chart -->
<section class="slide s7">
  <div class="stage"></div><div class="topline"></div>
  <span class="badge corner">QUARVEX</span>
  <h2 class="display chart-title" style="top:122px">Oval<br>Chart<br>Smart</h2>
  <svg width="418" height="234" style="position:absolute;left:0;top:0" font-family="Open Sans, sans-serif">
    <g fill="none" stroke-width="14" transform="rotate(-90 258 110)">
      <circle cx="258" cy="110" r="55" stroke="var(--aqua)" stroke-dasharray="121 346"/>
      <circle cx="258" cy="110" r="55" stroke="var(--sky)" stroke-dasharray="45 346" stroke-dashoffset="-121"/>
      <circle cx="258" cy="110" r="55" stroke="var(--blue)" stroke-dasharray="62 346" stroke-dashoffset="-166"/>
      <circle cx="258" cy="110" r="55" stroke="#5fc9cf" stroke-dasharray="118 346" stroke-dashoffset="-228"/>
    </g>
    <text x="258" y="112" text-anchor="middle" font-family="Bebas Neue, sans-serif" font-size="14" fill="var(--ink)">USA</text>
    <text x="258" y="120" text-anchor="middle" font-size="3.6" fill="#888">Add your summary text here,</text>
    <text x="258" y="125" text-anchor="middle" font-size="3.6" fill="#888">keep it to two short lines only.</text>
    <g stroke="var(--blue)" stroke-width="0.6" fill="none">
      <path d="M165 68h22l8 8"/><path d="M334 68h-12l-8 12"/><path d="M160 124h24"/><path d="M312 162l10 10h12"/><path d="M200 180h12l8-8"/>
    </g>
    <g fill="var(--blue)"><circle cx="195" cy="76" r="1.2"/><circle cx="314" cy="80" r="1.2"/><circle cx="184" cy="124" r="1.2"/><circle cx="312" cy="162" r="1.2"/><circle cx="220" cy="172" r="1.2"/></g>
    <g font-size="3.8" fill="#777">
      <rect x="213" y="188" width="3" height="3" fill="var(--aqua)"/><text x="218" y="191">1st Qtr</text>
      <rect x="235" y="188" width="3" height="3" fill="var(--sky)"/><text x="240" y="191">2nd Qtr</text>
      <rect x="258" y="188" width="3" height="3" fill="var(--blue)"/><text x="263" y="191">3rd Qtr</text>
      <rect x="280" y="188" width="3" height="3" fill="#5fc9cf"/><text x="285" y="191">4th Qtr</text>
    </g>
  </svg>
  <div class="donut-label" style="left:130px;top:52px"><b>23%</b>Lorem Ipsum</div>
  <div class="donut-label" style="left:335px;top:52px"><b>35%</b>Lorem Ipsum</div>
  <div class="donut-label" style="left:125px;top:112px"><b>19%</b>Lorem Ipsum</div>
  <div class="donut-label" style="left:336px;top:164px"><b>16%</b>Lorem Ipsum</div>
  <div class="donut-label" style="left:140px;top:172px"><b>21%</b>Lorem Ipsum</div>
  <span class="pageno">SLIDE / 7</span>
</section>

<!-- Table -->
<section class="slide s8">
  <div class="topline" style="left:0"></div>
  <span class="badge corner">QUARVEX</span>
  <h2 class="display table-title">Smart Table</h2>
  <table class="smart-table">
    <tr><th class="blank"></th><th style="background:#4cc3cc">Option 1</th><th style="background:#33b3cf">Option 2</th><th style="background:#0792cd">Option 3</th><th style="background:#1b8fc2">Option 4</th><th style="background:#2a9bcf">Option 5</th><th style="background:#0a7fb6">Option 6</th></tr>
    <tr><td class="rowhead">Row Sample 01</td><td>48</td><td>66</td><td>75</td><td>45</td><td>66</td><td>34</td></tr>
    <tr><td class="rowhead">Row Sample 02</td><td>35</td><td>75</td><td>89</td><td>58</td><td>48</td><td>66</td></tr>
    <tr><td class="rowhead">Row Sample 03</td><td>66</td><td>34</td><td>55</td><td>35</td><td>35</td><td>75</td></tr>
    <tr><td class="rowhead">Row Sample 04</td><td>55</td><td>70</td><td>84</td><td>52</td><td>55</td><td>35</td></tr>
    <tr><td class="rowhead">Row Sample 05</td><td>66</td><td>34</td><td>55</td><td>35</td><td>35</td><td>75</td></tr>
  </table>
  <span class="pageno">SLIDE / 8</span>
</section>

<!-- Callout connectors -->
<svg class="overlay" width="1200" height="1000">
  <polygon points="630,104 876,112 888,268 632,116" fill="rgba(8,52,78,.62)"/>
  <polygon points="188,677 872,578 868,664 188,683" fill="rgba(8,52,78,.62)"/>
</svg>

<!-- Stat callout -->
<div class="zoom zoom-stat">
  <svg width="304" height="304" style="position:absolute;left:0;top:0">
    <circle cx="152" cy="152" r="120" fill="none" stroke="var(--ice)" stroke-width="22" stroke-dasharray="377 754" transform="rotate(-90 152 152)"/>
    <circle cx="152" cy="152" r="104" fill="var(--blue)"/>
    <g fill="none" stroke="#fff" stroke-width="2.5">
      <path d="M152 140c-11-14-17-22-17-30a17 17 0 0 1 34 0c0 8-6 16-17 30z"/><circle cx="152" cy="110" r="6"/>
    </g>
  </svg>
  <span class="zoom-value">50%</span>
</div>

<!-- Photo callout -->
<div class="zoom zoom-photo" role="img" aria-label="Photo of a businessman seen from behind looking at a sunlit city skyline" style="background:linear-gradient(180deg,#f4e3e6 0%,#f7d3c4 45%,#f2b08a 70%,#e9c9bf 100%)"></div>
</body>
</html>
```